Web Design Project for hueframe

We are looking for a sleek and sophisticated website design for our already developed web-based gallery management software application. Here is a link to our web-app: http://www.hue-frame.co

You will login on the main page and then we would like to include all of the information on the PDF that I am providing below (it outlines what?, where?, why? who? and how much?). Basically, we need a home page, about page, and a pricing page, as well as a sign up page that should be navigable from the upper right hand corner of the site where the sign in/sign up would be located. Also, our 3 tenets are that the software program is "attractive, accessible, and affordable", which might need to be somehow incorporated. There are a few websites that we would like for you to take inspiration from listed below:

https://mybrolvex.com (for homepage)
https://pillowmantic.com (for homepage/pricing page/etc)
https://mybrolvex.com/tour (for a tour of how the product works)

We are currently having a logo designed and will share that as soon as it is available! Also, let us know if you need photos/screen shots, as we can provide them.

Thanks!

Target Market(s)

art galleries, artists, art collectors, art consultants, museums

Industry/Entity Type

Software

Requirements
Must have
• Home page
About page (or tour through the app)
Pricing page
Sign up page (the more click-throughs to signing up the better)

```html
<!DOCTYPE html>
<html lang="en">
<head>
<meta charset="utf-8">
<title>hueframe — Pricing</title>
<link href="https://fonts.googleapis.com/css2?family=Raleway:wght@300;400;500;600;700&family=Open+Sans:wght@700&display=swap" rel="stylesheet">
<style>
:root{
  --sky:#6dcff1;
  --sky-deep:#55c1ea;
  --footer:#88d5f0;
  --brand:#1b9bd1;
  --brand-dark:#0d84b6;
  --orange:#f7931e;
  --ink:#2e2e2e;
  --text:#555a5e;
  --muted:#8a8d90;
  --link:#1f6f94;
  --card-bg:#f9f9fa;
  --pill:#e4e4ea;
  --line:#dedede;
  --white:#ffffff;
}
*{box-sizing:border-box;margin:0;padding:0}
html,body{width:1200px;height:984px;overflow:hidden;background:var(--white)}
body{position:relative;font-family:"Raleway",Arial,sans-serif;color:var(--text)}
a{text-decoration:none;color:inherit}

.site-header{position:absolute;left:0;top:0;width:1200px;height:96px;
  background:linear-gradient(#ffffff,#f1f1f1);border-bottom:1px solid #cfd8dc}
.brand{position:absolute;left:70px;top:26px;display:flex;align-items:center;gap:12px;
  font-size:34px;font-weight:400;color:var(--brand);letter-spacing:.5px}
.brand-dot{width:30px;height:30px;border-radius:50%;background:var(--brand)}
.main-nav{position:absolute;left:343px;top:44px;display:flex;gap:27px;font-size:15.6px;font-weight:500;color:#8d8f91}
.main-nav .active{color:var(--brand)}
.auth{position:absolute;top:30px;display:flex;align-items:center;justify-content:center;height:40px;
  border-radius:4px;font-family:"Open Sans",Arial,sans-serif;font-weight:700;font-size:19px;letter-spacing:1.5px;color:var(--white)}
.auth-signin{left:922px;width:99px;background:var(--orange)}
.auth-signup{left:1032px;width:100px;background:var(--brand)}

.hero{position:absolute;left:0;top:96px;width:1200px;height:149px;
  background:linear-gradient(180deg,var(--sky) 0%,var(--sky-deep) 100%)}
.hero h1{position:absolute;left:69px;top:30px;font-weight:300;font-size:58px;color:var(--white);letter-spacing:.5px}

.perks{position:absolute;left:70px;top:310px;width:230px}
.perks h2{font-size:26px;font-weight:600;line-height:27px;color:var(--ink)}
.perks ul{list-style:none;margin-top:22px}
.perks li{position:relative;padding-left:18px;font-size:17px;line-height:32.4px;color:var(--text)}
.perks li::before{content:"";position:absolute;left:1px;top:13px;width:6px;height:6px;
  border-top:2px solid var(--brand);border-right:2px solid var(--brand);transform:rotate(45deg)}

.plan{position:absolute;top:305px;width:262px;height:374px;background:var(--card-bg);
  border:1px solid var(--line);border-radius:3px;box-shadow:0 1px 2px rgba(0,0,0,.08);text-align:center}
.plan-artist{left:310px}.plan-gallery{left:589px}.plan-web{left:868px}
.plan-head{height:62px;background:var(--white);border-bottom:1px solid var(--line);display:flex;align-items:center;justify-content:center;
  padding:0 24px;font-size:15px;font-weight:700;color:var(--brand);line-height:17px}
.plan-name{margin-top:16px;font-size:17px;font-weight:700;color:#7a7d80;line-height:18px;min-height:18px}
.price{display:inline-block;width:208px;height:38px;line-height:38px;background:var(--pill);border-radius:4px;
  font-size:25px;font-weight:700;color:var(--ink)}
.price-main{margin-top:16px}
.plan-web .price-main{margin-top:8px}
.plus{position:relative;width:24px;height:24px;margin:14px auto 0}
.plus::before,.plus::after{content:"";position:absolute;background:#8a8d90}
.plus::before{left:0;top:11px;width:24px;height:2px}
.plus::after{left:11px;top:0;width:2px;height:24px}
.activation{margin-top:16px;font-size:17px;font-weight:700;color:#7a7d80}
.plan-web .activation{margin-top:22px}
.price-setup{margin-top:15px}
.plan-web .price-setup{margin-top:10px}
.add-cart{position:absolute;left:2px;right:2px;bottom:2px;height:60px;line-height:60px;border-radius:3px;
  background:var(--brand);border-bottom:3px solid var(--brand-dark);color:var(--white);font-size:19px;font-weight:700}

.likes{position:absolute;left:506px;top:740px;display:flex;align-items:center;gap:7px;font-family:Arial,sans-serif;font-size:11px;color:#333}
.like-btn{height:25px;padding:0 6px;border:1px solid #c5cbd8;border-radius:2px;background:#eceef5;line-height:23px;color:#3b5998}
.like-mark{width:13px;height:13px;background:#3b5998}

.site-footer{position:absolute;left:0;top:794px;width:1200px;height:190px;background:var(--footer);text-align:center}
.footer-nav{position:absolute;left:158px;top:34px;display:flex;gap:40px;font-size:17px;font-weight:500;color:var(--link)}
.social{position:absolute;top:25px;width:40px;height:40px;border-radius:50%;border:2px solid var(--link);background:rgba(255,255,255,.12)}
.social-a{left:946px}.social-b{left:998px}
.footer-brand{position:absolute;left:0;right:0;top:96px;font-size:30px;font-weight:400;color:var(--link)}
.copyright{position:absolute;left:0;right:0;top:146px;font-size:17px;font-weight:500;letter-spacing:.5px;color:var(--link)}
</style>
</head>
<body>
<header class="site-header">
  <a class="brand" href="#"><span class="brand-dot"></span>hueframe</a>
  <nav class="main-nav">
    <a href="#">HOME</a><a href="#">ABOUT</a><a class="active" href="#">PRICING</a><a href="#">CONTAC US</a>
  </nav>
  <a class="auth auth-signin" href="#">SIGN IN</a>
  <a class="auth auth-signup" href="#">SIGN UP</a>
</header>

<section class="hero"><h1>Pricing</h1></section>

<aside class="perks">
  <h2>All system come with no contract</h2>
  <ul>
    <li>Unlimited access</li>
    <li>Access from any computer</li>
    <li>Mac or pc</li>
    <li>Unlimited storage</li>
    <li>Secure hosting</li>
    <li>Nightly backups</li>
  </ul>
</aside>

<article class="plan plan-artist">
  <div class="plan-head">ARTIST PRICING</div>
  <div class="plan-name">ARTIST PRICING</div>
  <div class="price price-main">$19 / Month</div>
  <div class="plus"></div>
  <div class="activation">NO ACTIVATION</div>
  <a class="add-cart" href="#">ADD TO CART</a>
</article>

<article class="plan plan-gallery">
  <div class="plan-head">GALLERY PRICING</div>
  <div class="plan-name">GALLERY PRICING</div>
  <div class="price price-main">$99 / Month</div>
  <div class="plus"></div>
  <div class="activation">ACTIVATION</div>
  <div class="price price-setup">$500 / Month</div>
  <a class="add-cart" href="#">ADD TO CART</a>
</article>

<article class="plan plan-web">
  <div class="plan-head">GALLERY WITH WEBSITE INTEGRATIO</div>
  <div class="plan-name">GALLERY WITH&nbsp; WEBSITE INTEGRATION</div>
  <div class="price price-main">$149 / Month</div>
  <div class="plus"></div>
  <div class="activation">ACTIVATION</div>
  <div class="price price-setup">$1500 / Month</div>
  <a class="add-cart" href="#">ADD TO CART</a>
</article>

<div class="likes">
  <span class="like-btn">Like</span>
  <span class="like-mark"></span>
  <span>8,165 people like this.</span>
</div>

<footer class="site-footer">
  <nav class="footer-nav">
    <a href="#">HOME</a><a href="#">ABOUT</a><a href="#">PRICING</a><a href="#">CONTAC US</a><a href="#">PRIVACY POLICY</a><a href="#">TERMS OF SERVICE</a>
  </nav>
  <a class="social social-a" href="#" aria-label="Social profile"></a>
  <a class="social social-b" href="#" aria-label="Social profile"></a>
  <div class="footer-brand">hueframe</div>
  <p class="copyright">© 2013 HUEFRAME. ALL RIGHTS RESERVED.</p>
</footer>
</body>
</html>
```